eBook Cover_H. Vollmar-Tessen
Schnell und zuverlässoig,Änderungswünsche wurden umgehend ausgeführt. Vielen Dank für das tolle Cover zu meinem ersten Buch!
Zielgruppe
freie Roman-Autorin (Erstlingswerk)
Zielgruppe: Lesende (Erwachsene), Frauen
Charakterisierung: magisch-realistischer Familienroman, spielt im Europa der Jetzt-Zeit
Aufgabenstellung
Im ersten Schritt geht es um ein Cover für ein eBook, das aber bei Bedarf als Book on Demand gedruckt werden soll. Es wird daher später Anforderung bzgl. Dicke / Umfang des gedruckten Buches und einer Rückseite geben. Das gewählte Design soll dann dahingehend überarbeitet und finale Druckdaten zur Verfügung gestellt werden. Dies soll von vornherein berücksichtigt werden und im Preis enthalten sein.
Titel: Nebel über Glas, Funken im Moor
Autorinnenname: Henrike Vollmar-Tessen
des weiteren auf dem Cover: Roman

```html
<!DOCTYPE html>
<html lang="de">
<head>
<meta charset="utf-8">
<title>Nebel über Glas, Funken im Moor – Henrike Vollmar-Tessen</title>
<link rel="stylesheet" href="https://fonts.googleapis.com/css2?family=Oswald:wght@600&family=Open+Sans:wght@400&display=swap">
<style>
  :root {
    --paper: #ffffff;
    --ink: #56616b;
    --frame: #5f6a73;
    --red-deep: #a80d02;
    --red-mid: #e0290a;
    --red-bright: #f4501c;
    --label: #ffffff;
  }
  html, body {
    margin: 0;
    padding: 0;
    width: 841px;
    height: 1200px;
    overflow: hidden;
    background: var(--paper);
  }
  .cover {
    position: relative;
    width: 841px;
    height: 1200px;
    background: var(--paper);
    overflow: hidden;
  }
  .cover__artwork {
    position: absolute;
    inset: 0;
    width: 841px;
    height: 1200px;
    display: block;
  }
  .cover__author {
    position: absolute;
    left: 394px;
    top: 379px;
    width: 379px;
    height: 64px;
    box-sizing: border-box;
    border: 2px solid var(--frame);
    display: flex;
    align-items: center;
    justify-content: center;
    font-family: "Open Sans", sans-serif;
    font-size: 25px;
    color: var(--ink);
    letter-spacing: 0.5px;
    white-space: nowrap;
  }
  .cover__title {
    position: absolute;
    left: 345px;
    top: 520px;
    width: 490px;
    margin: 0;
    font-family: "Oswald", sans-serif;
    font-weight: 600;
    font-size: 64px;
    line-height: 76px;
    letter-spacing: 2px;
    color: var(--ink);
    text-align: center;
    text-transform: uppercase;
  }
  .cover__title span { display: block; }
  .cover__genre {
    position: absolute;
    left: 96px;
    bottom: 22px;
    margin: 0;
    font-family: "Oswald", sans-serif;
    font-weight: 600;
    font-size: 62px;
    line-height: 1;
    letter-spacing: 2px;
    color: var(--label);
  }
</style>
</head>
<body>
<main class="cover">
  <svg class="cover__artwork" viewBox="0 0 841 1200" role="img" aria-label="Abstrakte rote Grafik mit geschwungenen Linienbündeln und leuchtenden Kreisen">
    <defs>
      <linearGradient id="red-glow" x1="0" y1="0" x2="1" y2="1">
        <stop offset="0" stop-color="var(--red-deep)"/>
        <stop offset="0.35" stop-color="var(--red-mid)"/>
        <stop offset="0.55" stop-color="var(--red-bright)"/>
        <stop offset="0.8" stop-color="var(--red-mid)"/>
        <stop offset="1" stop-color="var(--red-deep)"/>
      </linearGradient>
    </defs>
    <polygon points="0,0 423,0 310,591 420,1200 0,1200" fill="url(#red-glow)"/>
  </svg>

  <div class="cover__author">HENRIKE VOLLMAR-TESSEN</div>

  <h1 class="cover__title">
    <span>Nebel über Glas</span>
    <span>Funken im Moor</span>
  </h1>

  <p class="cover__genre">ROMAN</p>
</main>
</body>
</html>
```